Landfill Gas-to-Renewable Natural Gas business

We have a website ( corvelmetharoutes .com via Net Burrow) that needs to be revamped.

We have three RNG projects in Puerto Rico (Humacao, Ponce, Salinas), that take landfill gas (LFG) and produce renewable liquid natural gas (R-LNG) for companies looking to offset their carbon emissions (footprint). We also produce a renewable carbon dioxide (R-CO2) that can be reused for industrial CO2 purposes. All CO2 is imported to the island, so reusing CO2 on the island further reduces global CO2 emissions. The design should reflect renewables, sustainability, professionalism, safety and experience in this sector.

Sites with RNG examples:
https://www.qx.com/en_us/united-states/home/what-we-do/production-and-operations/tolvane-fuels.html
https://brambleflowco.com/
http://kessfordpower.com/operations/
https://wyndcastle.com/
https://www.tamberhold.com/
https://pexloweco.com/
https://sandmoorbiolines.com/
https://curvetto.com/
https://www.dolvatri.com/renewable-natural-gas/
https://www.haskipowerworks.com/

Renewables Natural Gas, Sustainability,

4 page

• Health, Safety, Environment (HSE) aspect. Industry experience section, about us, photos, landfill gas, LNG, RNG, CO2

```html
<!DOCTYPE html>
<html lang="en">
<head>
<meta charset="utf-8">
<title>Corvel Metharoutes — Island Sourced Waste-to-Energy</title>
<link rel="stylesheet" href="https://fonts.googleapis.com/css2?family=Montserrat:wght@300;400;500;600;700;800&family=EB+Garamond:wght@500&display=swap">
<style>
:root{
  --navy:#262a6b;
  --navy-deep:#2a2763;
  --blue:#1a6be8;
  --green:#0cd66e;
  --white:#ffffff;
  --text:#3a3a4a;
  --muted:#e9ebf5;
}
*{margin:0;padding:0;box-sizing:border-box}
html,body{width:1200px;height:5186px;overflow:hidden;background:var(--white)}
body{position:relative;font-family:'Montserrat',sans-serif;color:var(--text)}
.abs{position:absolute}
.ph{position:absolute;display:block}

/* header */
.brand{left:128px;top:16px;display:flex;align-items:center;gap:12px}
.brand-dot{width:62px;height:62px;border-radius:50%;background:var(--blue)}
.brand-name{font-family:'Montserrat',sans-serif;font-weight:400;font-size:24px;line-height:27px;color:var(--navy)}
.top-btn{top:0;height:46px;display:flex;align-items:center;justify-content:center;color:var(--white);font-weight:700;font-size:15px;letter-spacing:.3px}
.btn-call{left:707px;width:211px;background:var(--blue)}
.btn-start{left:924px;width:159px;background:var(--green)}
.nav{top:78px;left:0;width:1200px;height:20px}
.nav a{position:absolute;font-size:15px;font-weight:600;color:var(--navy);text-decoration:none}

/* hero */
.hero{left:0;top:124px;width:1200px;height:548px;background:linear-gradient(180deg,#8fb0cf 0%,#c9d6e2 45%,#7f8f6c 70%,#5f6a52 100%)}
.hero-title{left:706px;top:296px;font-size:43px;font-weight:800;line-height:50px;color:var(--white)}
.pill{display:flex;align-items:center;justify-content:center;border-radius:30px;color:var(--white);font-weight:700;font-size:16px}
.hero-btn{left:706px;top:416px;width:170px;height:56px;background:var(--blue)}

/* section titles */
.sec-title{left:0;width:1200px;text-align:center;font-size:34px;font-weight:800;color:var(--navy)}
.sec-lead{left:0;width:1200px;text-align:center;font-size:14px;line-height:20px;color:var(--text)}

.project-label{top:1272px;font-size:20px;font-weight:600;color:#333;text-align:center}

/* industry */
.industry-panel{left:562px;top:1446px;width:638px;height:549px;background:var(--green)}
.industry-title{left:613px;top:1556px;font-size:36px;line-height:44px;font-weight:800;color:var(--white)}
.industry-text{left:613px;top:1674px;width:455px;font-size:15px;line-height:24px;color:var(--white)}

/* values band */
.values{left:0;top:2025px;width:1200px;height:355px;background:var(--blue)}
.value{top:2130px;width:220px;text-align:center;color:var(--white)}
.value svg{display:block;margin:0 auto 18px;width:100px;height:100px}
.value span{font-size:21px;font-weight:700}

/* about */
.about-title{left:128px;top:2508px;font-size:36px;font-weight:800;color:var(--navy)}
.about-text{left:128px;top:2564px;width:420px;font-size:15px;line-height:24px;color:var(--text)}
.about-btn{left:128px;top:2850px;width:170px;height:54px;background:var(--green)}

.produce-title{left:208px;top:3052px;font-family:'EB Garamond',serif;font-weight:500;font-size:32px;line-height:40px;color:var(--navy)}

/* what we do */
.wwd{left:0;top:3595px;width:1200px;height:610px;background:var(--navy-deep)}
.service{top:3771px;width:260px;text-align:center;color:var(--white)}
.service .ph{position:relative;margin:0 auto;width:224px;height:224px;border-radius:50%}
.service h3{margin-top:28px;font-size:18px;font-weight:800}
.service p{margin-top:8px;font-size:14px;line-height:17px}

/* footer */
.footer{left:0;top:4805px;width:1200px;height:381px;background:var(--navy-deep)}
.foot-brand{left:128px;top:4898px;display:flex;align-items:center;gap:14px}
.foot-brand .brand-name{color:var(--white);font-size:29px;line-height:32px}
.foot-brand .brand-dot{width:72px;height:72px;background:var(--green)}
.divider{width:1px;height:145px;background:rgba(255,255,255,.45);top:4855px}
.foot-head{top:4880px;font-size:17px;font-weight:700;color:var(--white)}
.foot-links a{position:absolute;font-size:15px;color:var(--white);text-decoration:none}
.pin{left:730px;top:4930px;width:48px;height:48px;border-radius:50%;background:var(--green);display:flex;align-items:center;justify-content:center}
.address{left:790px;top:4935px;width:330px;font-size:14px;line-height:18px;color:var(--white)}
.copyright{left:0;top:5106px;width:1200px;text-align:center;font-size:14px;color:var(--white)}
</style>
</head>
<body>

<header>
  <div class="abs brand"><span class="brand-dot"></span><span class="brand-name">Corvel<br>Metharoutes</span></div>
  <a class="abs top-btn btn-call">CALL: 555 014 2290</a>
  <a class="abs top-btn btn-start">GET STARTED</a>
  <nav class="abs nav">
    <a style="left:465px">What is RNG?</a>
    <a style="left:630px">Benefits</a>
    <a style="left:753px">About Us</a>
    <a style="left:883px">Projects</a>
    <a style="left:1007px">Contact</a>
  </nav>
</header>

<section>
  <div class="ph hero" role="img" aria-label="Photo of a gas processing plant with tall steel columns under a cloudy sky beside green fields"></div>
  <h1 class="abs hero-title">ISLAND SOURCED<br>WASTE-TO-ENERGY</h1>
  <a class="abs pill hero-btn">CONTACT US</a>
</section>

<section>
  <h2 class="abs sec-title" style="top:745px">RNG PROJECTS</h2>
  <p class="abs sec-lead" style="top:800px">Lorem ipsum dolor sit amet, consectetur adipiscing elit, sed do eiusmod<br>tempor incididunt ut labore et dolore magna aliquuis ipsum</p>
  <div class="ph" style="left:129px;top:888px;width:287px;height:356px;background:linear-gradient(180deg,#d6e2ec 0%,#c2cbd2 60%,#7d9a4e 85%,#6a8a3c 100%)" role="img" aria-label="Photo of the Humacao gas plant"></div>
  <div class="ph" style="left:431px;top:888px;width:337px;height:356px;background:linear-gradient(160deg,#2e5a63 0%,#44636a 40%,#c9c6c0 65%,#8a8378 100%)" role="img" aria-label="Aerial photo of the Ponce storage tanks by the sea"></div>
  <div class="ph" style="left:785px;top:888px;width:286px;height:356px;background:linear-gradient(180deg,#6d9cc9 0%,#b7cfe2 45%,#9aa5ad 70%,#4f7a3e 100%)" role="img" aria-label="Photo of the Salinas power plant with a tall stack"></div>
  <div class="abs project-label" style="left:129px;width:287px">Humacao</div>
  <div class="abs project-label" style="left:431px;width:337px">Ponce</div>
  <div class="abs project-label" style="left:785px;width:286px">Salinas</div>
</section>

<section>
  <div class="ph" style="left:0;top:1446px;width:562px;height:549px;background:linear-gradient(180deg,#5fa7e0 0%,#a9d2ef 40%,#5dae68 62%,#7fbf3f 100%)" role="img" aria-label="Photo of green biogas digester tanks on a grassy field"></div>
  <div class="abs industry-panel"></div>
  <h2 class="abs industry-title">INDUSTRY<br>EXPERIENCE</h2>
  <p class="abs industry-text">Lorem ipsum dolor sit amet, consectetur adipiscing elit, sed do eiusmod tempor incididunt ut labore et dolore magna aliqua. Quis ipsum suspendisse ultrices gravida. Risuscom m odo viverra maecenas accumsan lacus vel facilisisorem ipsum dolor sit amet, consectetur adipiscing elit, sed do eiusmod tempor incididunt ut labore et dolore magna aliqu uis ipsum suspendisse ultrices gravidaisuscom m odo viv erra maecenas accumsan lacus vel facilisis.</p>
</section>

<section>
  <div class="abs values"></div>
  <div class="abs value" style="left:72px">
    <svg viewBox="0 0 100 100" fill="none" stroke="#fff" stroke-width="3" stroke-linecap="round"><circle cx="50" cy="42" r="20"/><path d="M42 62v12h16V62M44 80h12M50 10v8M22 22l6 6M78 22l-6 6M14 44h8M78 44h8M50 62V44M50 52c-6-2-9-7-8-12 6 1 9 6 8 12zM50 50c5-2 8-6 7-11-5 1-8 5-7 11z"/></svg>
    <span>Renewables</span>
  </div>
  <div class="abs value" style="left:283px">
    <svg viewBox="0 0 100 100" fill="none" stroke="#fff" stroke-width="3" stroke-linecap="round"><circle cx="44" cy="28" r="14"/><path d="M16 84V70c0-10 10-18 28-18 8 0 14 2 18 4"/><circle cx="72" cy="72" r="12"/><path d="M66 72l4 4 8-8"/></svg>
    <span>Professionalism</span>
  </div>
  <div class="abs value" style="left:518px">
    <svg viewBox="0 0 100 100" fill="none" stroke="#fff" stroke-width="3" stroke-linecap="round"><circle cx="52" cy="40" r="18"/><path d="M52 22v-8M52 14c-6 0-10-4-10-8 6 0 10 4 10 8zM52 14c6 0 10-4 10-8-6 0-10 4-10 8zM10 64l14-6c6-2 10 0 16 2h16c4 0 4 6 0 6H42M24 84l10-6h22l28-20c4-2 7 2 4 5L62 86H30"/></svg>
    <span>Sustainability</span>
  </div>
  <div class="abs value" style="left:710px">
    <svg viewBox="0 0 100 100" fill="none" stroke="#fff" stroke-width="3" stroke-linecap="round" stroke-linejoin="round"><path d="M50 12l20 8v16c0 14-9 24-20 28-11-4-20-14-20-28V20z"/><path d="M42 38l6 6 10-12M12 40v22l16 16v10M88 40v22L72 78v10M22 56l12 12M78 56L66 68"/></svg>
    <span>Safety</span>
  </div>
  <div class="abs value" style="left:911px">
    <svg viewBox="0 0 100 100" fill="none" stroke="#fff" stroke-width="3" stroke-linecap="round"><circle cx="40" cy="54" r="12"/><path d="M40 28v8M40 72v8M14 54h8M58 54h8M22 36l6 6M58 72l-6-6M22 72l6-6M58 36l-6 6"/><circle cx="68" cy="66" r="14"/><path d="M61 66l5 5 9-9M60 36V16h10c4 0 4 6 0 6h8c4 0 4 6 0 6h6v10H66"/></svg>
    <span>Experience</span>
  </div>
</section>

<section>
  <h2 class="abs about-title">ABOUT US</h2>
  <p class="abs about-text">Lorem ipsum dolor sit amet, consectetur adipiscing elit, sed do eiusmod tempor incididunt ut labore et dolore magna aliqua. Ut enim ad minim veniam, quis nostrud exercitation ullamco laboris nisi ut aliquip ex ea comm odo consequat. Duis aute irure dolor in reprehenderit in voluptate velit esse cillum dolore eu fugiat nulla paria tur. Excepteur sint occaecat cupidatat non proid ent, sunt in culpa qui officia deserunt mollit anim id loest labor umLorem ipsum dolor sit amet, consectetur adip iscing elit, sed do eiusmod tempor incididunt ut labo re et dolore magna aliqut enim ad minim.</p>
  <a class="abs pill about-btn">READ MORE</a>
  <div class="ph" style="left:628px;top:2499px;width:444px;height:444px;border-radius:50%;background:linear-gradient(180deg,#5c9ad6 0%,#b9d3ea 40%,#8d9aa6 65%,#3e5a86 100%)" role="img" aria-label="Photo of an industrial gas treatment unit with a tall stack"></div>
</section>

<section>
  <h2 class="abs produce-title">Corvel Metharoutes will Produce Renewable<br>Natural Gas, Renewable CO2 and Power from Landfill Gas</h2>
  <div class="ph" style="left:0;top:3180px;width:1200px;height:345px;background:linear-gradient(180deg,#ffffff 0%,#f4f4f6 45%,#9a3f26 78%,#8a3a22 100%)" role="img" aria-label="Illustration of landfill gas flowing from landfill wells through moisture removal, gas separation and compression to RNG delivery trucks and industrial and commercial customers"></div>
</section>

<section>
  <div class="abs wwd"></div>
  <h2 class="abs sec-title" style="top:3668px;color:var(--white)">WHAT WE DO</h2>
  <div class="abs service" style="left:94px">
    <div class="ph" style="background:linear-gradient(180deg,#7fa6c9 0%,#9aa68a 45%,#4e6e3a 100%)" role="img" aria-label="Aerial photo of landfill gas digesters"></div>
    <h3>LANDFILL GAS</h3>
    <p>Lorem ipsum dolor sitac<br>onsectetur adipiscing elits<br>ed do eiusmod tempo.</p>
  </div>
  <div class="abs service" style="left:345px">
    <div class="ph" style="background:linear-gradient(180deg,#a9c6e4 0%,#e6eaee 50%,#8f9b86 100%)" role="img" aria-label="Photo of a white LNG storage tank"></div>
    <h3>LNG</h3>
    <p>Lorem ipsum dolor sitac<br>onsectetur adipiscing elits<br>ed do eiusmod tempo.</p>
  </div>
  <div class="abs service" style="left:596px">
    <div class="ph" style="background:linear-gradient(180deg,#6aa3d8 0%,#c8d3dc 55%,#6d7f5a 100%)" role="img" aria-label="Photo of RNG processing columns"></div>
    <h3>RNG</h3>
    <p>Lorem ipsum dolor sitac<br>onsectetur adipiscing elits<br>ed do eiusmod tempo.</p>
  </div>
  <div class="abs service" style="left:847px">
    <div class="ph" style="background:linear-gradient(180deg,#c7d4df 0%,#6e7880 55%,#2f3a40 100%)" role="img" aria-label="Photo of industrial stacks releasing CO2 emissions"></div>
    <h3>CO2</h3>
    <p>Lorem ipsum dolor sitac<br>onsectetur adipiscing elits<br>ed do eiusmod tempo.</p>
  </div>
</section>

<section>
  <h2 class="abs sec-title" style="top:4283px">GALLERY</h2>
  <div class="ph" style="left:56px;top:4370px;width:252px;height:320px;background:linear-gradient(180deg,#dfe3e6 0%,#b3b8bb 55%,#7c7f7f 100%)" role="img" aria-label="Gallery photo of gas equipment enclosures"></div>
  <div class="ph" style="left:334px;top:4370px;width:252px;height:320px;background:linear-gradient(180deg,#d9dde0 0%,#aab1b6 50%,#6f777c 100%)" role="img" aria-label="Gallery photo of steel process vessels"></div>
  <div class="ph" style="left:613px;top:4370px;width:252px;height:320px;background:linear-gradient(180deg,#8d8a84 0%,#b8b5ad 50%,#5b5a56 100%)" role="img" aria-label="Gallery photo of plant piping"></div>
  <div class="ph" style="left:892px;top:4370px;width:252px;height:320px;background:linear-gradient(180deg,#a8c8e8 0%,#8ea2b4 50%,#3e4d66 100%)" role="img" aria-label="Gallery photo of a refinery structure"></div>
</section>

<footer>
  <div class="abs footer"></div>
  <div class="abs foot-brand"><span class="brand-dot"></span><span class="brand-name">Corvel<br>Metharoutes</span></div>
  <div class="abs divider" style="left:422px"></div>
  <div class="abs foot-head" style="left:462px">LINKS</div>
  <div class="foot-links">
    <a class="abs" style="left:461px;top:4922px">Home</a>
    <a class="abs" style="left:461px;top:4947px">About</a>
    <a class="abs" style="left:461px;top:4972px">projects</a>
    <a class="abs" style="left:558px;top:4924px">Services</a>
    <a class="abs" style="left:558px;top:4949px">FAQ</a>
    <a class="abs" style="left:558px;top:4974px">Contact</a>
  </div>
  <div class="abs divider" style="left:678px"></div>
  <div class="abs foot-head" style="left:730px">CONTACT</div>
  <div class="abs pin"><svg width="20" height="24" viewBox="0 0 20 24"><path d="M10 0C4.5 0 0 4.4 0 9.8 0 17 10 24 10 24s10-7 10-14.2C20 4.4 15.5 0 10 0z" fill="#fff"/><circle cx="10" cy="9.5" r="3.5" fill="#0cd66e"/></svg></div>
  <p class="abs address">Calle Brisa Alta 118, Suite 204, San Juan, Puerto Rico 00900</p>
  <p class="abs copyright">Copyright © 2025 Corvel Metharoutes. All Rights Reserved.</p>
</footer>

</body>
</html>
```